VantoMedix website

I have a plumtree hosting website already & have been using wordpress.
See www.vantomedix-example.com
I have a logo's already.
I need a front page "VantoMedix". I have 3 products: (need separate pages)
1) the "GlideDeck" (can't supply images ATM)
2) the "CordKeeper" (several stills below & animation: http://www.videohub-example.com/watch?v=X7KpR2mT9wQ&list=ZPqR8bT_vnxwyLmKcE4D7T_B&feature=share)
3) the "FastWedge" animation here: http://vidhub-example.be/pqwre-Lmm_Z & logo as below

It needs to be corporate & professional looking. VantoMedix is an innovative design house for medical devices.

Reason: Hi Designers, thanks for all your work to date - there have been some great designs. We'll be providing feedback to some of you in the near future. The reason we have extended the deadline is simply that we are too busy with other aspects of the business to focus on this at the moment. Kind regards, the VantoMedix team.

Dear Designers,

VantoMedix apologies for the delay due to our busyness. 
Please help us to understand the process here:
are we getting fully working websites? With multiple pages? Will we be able to modify them?
If not, what is the output?

Kind regards,
the Vanto team.

```html
<!DOCTYPE html>
<html lang="en">
<head>
<meta charset="utf-8">
<title>VantoMedix</title>
<link href="https://fonts.googleapis.com/css2?family=Ubuntu:wght@400;500;700&family=Roboto:ital,wght@0,400;0,500;1,400&display=swap" rel="stylesheet">
<style>
:root{
  --blue:#2fa9e0;
  --blue-dark:#1e8fc4;
  --orange:#f26a22;
  --ink:#333333;
  --text:#555555;
  --grey-card:#666666;
  --footer:#333333;
  --line:#dddddd;
  --white:#ffffff;
}
*{box-sizing:border-box;margin:0;padding:0}
html,body{width:1097px;height:1200px;overflow:hidden;background:var(--white)}
body{position:relative;font-family:'Roboto',Arial,sans-serif;color:var(--text)}
.abs{position:absolute}
a{color:inherit;text-decoration:none}

/* header */
.brand{left:137px;top:14px;display:flex;align-items:center;gap:8px}
.brand-dot{width:20px;height:20px;border-radius:50%;background:var(--blue)}
.brand-name{font-family:'Ubuntu',sans-serif;font-weight:700;font-size:40px;color:var(--blue);letter-spacing:-1px}
.call{left:800px;top:19px;display:flex;gap:10px;align-items:center}
.call-text{font-family:'Ubuntu',sans-serif;font-size:14px;color:#666;line-height:17px}

/* nav */
.nav{left:0;top:77px;width:1097px;height:35px;background:var(--blue);border-bottom:2px solid var(--blue-dark)}
.nav ul{list-style:none;position:absolute;left:137px;top:0;display:flex;height:35px}
.nav li{font-family:'Ubuntu',sans-serif;font-weight:500;font-size:16px;color:var(--white);display:flex;align-items:center;justify-content:center;border-right:1px solid #6ec4ea;height:35px}
.nav li.active{background:var(--orange)}

/* hero */
.hero{left:0;top:112px;width:1097px;height:432px;background:linear-gradient(90deg,#c9dcea 0%,#e8f1f8 35%,#f4f8fb 60%,#e6eff7 100%)}
.card{width:257px;height:172px;top:350px;background:var(--white);padding:5px;box-shadow:0 1px 4px rgba(0,0,0,.35)}
.card-img{height:90px;width:100%}
.card-body{height:72px;background:var(--grey-card);color:var(--white);padding:8px 12px;position:relative}
.card.active .card-body{background:var(--blue)}
.card-title{font-family:'Ubuntu',sans-serif;font-weight:500;font-size:17px;margin-bottom:4px}
.card-text{font-size:11.5px;line-height:14px}
.card-more{position:absolute;right:14px;bottom:5px;font-size:10px;font-style:italic;color:var(--orange)}

/* about */
.about-title{left:0;top:566px;width:1097px;text-align:center;font-family:'Ubuntu',sans-serif;font-weight:500;font-size:30px;color:var(--ink)}
.about-title span{color:var(--blue);font-weight:700}
.about-text{left:137px;top:610px;width:823px;text-align:center;font-family:'Ubuntu',sans-serif;font-size:14px;line-height:18px;color:#666}
.read-more{left:0;top:675px;width:1097px;text-align:center;font-family:'Ubuntu',sans-serif;font-size:14px;color:var(--blue)}

.sec-head{display:flex;align-items:center;gap:10px;font-family:'Ubuntu',sans-serif;font-size:20px;color:var(--orange)}
.sec-dot{width:22px;height:22px;border-radius:50%;border:5px solid var(--blue)}

.chart{left:137px;top:757px;width:285px;height:129px;border:1px solid #ddd;box-shadow:0 1px 3px rgba(0,0,0,.2);background:var(--white)}
.facts{left:430px;top:758px;width:232px;list-style:none}
.facts li{display:flex;gap:12px;font-size:11.5px;line-height:14px;color:#666;margin-bottom:13px}
.facts-rule{left:430px;top:885px;width:222px;border-top:1px dotted #bbb}
.facts-more{left:586px;top:900px;font-size:11.5px;color:var(--orange)}
.divider{left:672px;top:715px;width:1px;height:200px;background:linear-gradient(#fff,#ddd 30%,#ddd 70%,#fff)}

.news{left:694px;width:266px;display:flex;gap:9px;border-bottom:1px solid #e4e4e4;padding-bottom:12px}
.news-date{width:43px;height:43px;background:var(--blue);color:var(--white);text-align:center;font-family:'Ubuntu',sans-serif;flex:none;padding-top:3px}
.news-date b{display:block;font-size:19px;font-weight:400;line-height:20px}
.news-date i{font-style:normal;font-size:13px;line-height:15px}
.news h4{font-family:'Ubuntu',sans-serif;font-weight:500;font-size:12.5px;color:var(--ink);margin-bottom:2px}
.news p{font-size:11px;line-height:12px;color:#666}
.more-news{left:902px;top:900px;font-size:11px;color:var(--orange);text-decoration:underline}

/* footer */
.footer{left:0;top:935px;width:1097px;height:234px;background:var(--footer)}
.f-head{font-family:'Ubuntu',sans-serif;font-weight:500;font-size:18px;color:var(--white)}
.testi{left:138px;top:993px;width:316px;height:129px;background:var(--white);border-radius:6px}
.testi-photo{position:absolute;left:34px;top:32px;width:60px;height:62px;background:linear-gradient(#6b4a3a,#3a2a22)}
.testi-quote{position:absolute;left:103px;top:30px;width:195px;font-style:italic;font-size:12px;line-height:17px;color:#444}
.testi-name{position:absolute;left:103px;top:91px;font-size:12.5px;color:var(--ink)}
.testi-name span{color:var(--blue)}
.links{list-style:none}
.links li{font-size:11px;color:var(--white);height:28.3px}
.follow li{display:flex;gap:9px;align-items:center}
.follow a{text-decoration:underline;color:#ddd}
.soc{width:17px;height:17px;border-radius:2px;flex:none}
.field{left:764px;width:196px;height:20px;background:#f2f2f2;border:1px solid #ccc;font-size:10.5px;font-style:italic;color:#777;padding:3px 7px}
.submit{left:764px;top:1125px;width:66px;height:21px;background:var(--blue);color:var(--white);font-family:'Ubuntu',sans-serif;font-weight:500;font-size:14px;text-align:center;line-height:21px;border-radius:2px}
.copy{left:0;top:1169px;width:1097px;height:31px;background:var(--orange);color:var(--white);text-align:center;font-size:11.5px;line-height:31px}
</style>
</head>
<body>

<header>
  <div class="abs brand"><span class="brand-dot"></span><span class="brand-name">VantoMedix</span></div>
  <div class="abs call">
    <svg width="30" height="30" viewBox="0 0 24 24"><path fill="#f26a22" d="M6.6 10.8a15.1 15.1 0 0 0 6.6 6.6l2.2-2.2c.3-.3.7-.4 1-.2 1.1.4 2.3.6 3.6.6.6 0 1 .4 1 1V20c0 .6-.4 1-1 1A17 17 0 0 1 3 4c0-.6.4-1 1-1h3.5c.6 0 1 .4 1 1 0 1.3.2 2.5.6 3.6.1.3 0 .7-.2 1z"/></svg>
    <div class="call-text">Call Us<br>+61 (0) 4000 18265</div>
  </div>
</header>

<nav class="abs nav">
  <ul>
    <li class="active" style="width:135px">Home</li>
    <li style="width:139px">About</li>
    <li style="width:167px">Producsts</li>
    <li style="width:206px">Ask A Question</li>
    <li style="width:176px">Contact Us</li>
  </ul>
</nav>

<section class="abs hero" role="img" aria-label="Gloved hand touching a medical interface with circular icons of a cross, heart, person and globe over a faint world network map"></section>

<article class="abs card active" style="left:137px">
  <div class="card-img" role="img" aria-label="Wiring diagram of a switch box connecting a PC, projector and board" style="background:linear-gradient(#f4f4f4,#dcdcdc)"></div>
  <div class="card-body">
    <div class="card-title">GlideDeck</div>
    <div class="card-text">Lorem ipsum dolor sit amet, consectetuer adipiscing elit, sed diam</div>
    <div class="card-more">more ▸</div>
  </div>
</article>
<article class="abs card" style="left:421px">
  <div class="card-img" role="img" aria-label="Rendered device clipped to a stretcher rail" style="background:linear-gradient(160deg,#2a2a2a,#5c5c6a 55%,#8a86a8)"></div>
  <div class="card-body">
    <div class="card-title">CordKeeper</div>
    <div class="card-text">Lorem ipsum dolor sit amet, consectetuer adipiscing elit, sed diam</div>
    <div class="card-more">more ▸</div>
  </div>
</article>
<article class="abs card" style="left:704px">
  <div class="card-img" role="img" aria-label="Red hatchback with open door showing a seated patient" style="background:linear-gradient(#c8c8c8,#b8342a 45%,#9a2a22 75%,#bdbdbd)"></div>
  <div class="card-body">
    <div class="card-title">FastWedge</div>
    <div class="card-text">Lorem ipsum dolor sit amet, consectetuer adipiscing elit, sed diam</div>
    <div class="card-more">more ▸</div>
  </div>
</article>

<section>
  <h1 class="abs about-title">About <span>VantoMedix</span></h1>
  <p class="abs about-text">Lorem ipsum dolor sit amet, consectetuer adipiscing elit, sed diam nonummy nibh euismod tincidunt ut laoreet dolore magna aliquam erat volutpat. Ut wisi enim ad minim veniam, quis nostrud exerci tation ullamcorper suscipit nisl ut aliquip ex ea commodo consequat. Duis autem vel eum iriure dolor in hendrerit</p>
  <a class="abs read-more">Read More [ + ]</a>
</section>

<h2 class="abs sec-head" style="left:137px;top:709px"><span class="sec-dot"></span>Did You Know ?</h2>
<h2 class="abs sec-head" style="left:694px;top:709px"><span class="sec-dot"></span>Latest News</h2>

<div class="abs chart">
  <svg width="285" height="129" viewBox="0 0 285 129" font-family="Arial" font-size="6" fill="#444">
    <text x="142" y="22" text-anchor="middle" font-weight="bold">Occupational Injury Rates per 100 FT workers per year</text>
    <g stroke="#e6e6e6" stroke-width=".6">
      <line x1="26" y1="8" x2="278" y2="8"/><line x1="26" y1="23" x2="278" y2="23"/><line x1="26" y1="38" x2="278" y2="38"/><line x1="26" y1="53" x2="278" y2="53"/><line x1="26" y1="68" x2="278" y2="68"/><line x1="26" y1="83" x2="278" y2="83"/><line x1="26" y1="98" x2="278" y2="98"/><line x1="26" y1="113" x2="278" y2="113"/>
    </g>
    <g text-anchor="end"><text x="20" y="10">40</text><text x="20" y="25">35</text><text x="20" y="40">30</text><text x="20" y="55">25</text><text x="20" y="70">20</text><text x="20" y="85">15</text><text x="20" y="100">10</text><text x="20" y="115">5</text></g>
    <rect x="44" y="40" width="55" height="75" fill="#5d7f92" role="img" aria-label="Illustration of a human back with highlighted spine"/>
    <g fill="#5b9bd5"><rect x="42" y="110" width="16" height="18"/><rect x="90" y="106" width="16" height="22"/><rect x="138" y="86" width="16" height="42"/><rect x="186" y="71" width="16" height="57"/></g>
    <rect x="234" y="23" width="16" height="105" fill="#ffc000"/>
  </svg>
</div>

<ul class="abs facts">
  <li><svg width="18" height="14" viewBox="0 0 18 14"><path d="M1 7l5 5L17 1" stroke="#2fa9e0" stroke-width="3" fill="none"/></svg><span>The cost of paramedic (EMS) injury in Australia is over $32,000 dollars a day?</span></li>
  <li><svg width="18" height="14" viewBox="0 0 18 14"><path d="M1 7l5 5L17 1" stroke="#2fa9e0" stroke-width="3" fill="none"/></svg><span>(That translates to well over half a billion dollars every year globally.)</span></li>
  <li><svg width="18" height="14" viewBox="0 0 18 14"><path d="M1 7l5 5L17 1" stroke="#2fa9e0" stroke-width="3" fill="none"/></svg><span>17% of injured paramedics remain off duty for over a month?</span></li>
</ul>
<div class="abs facts-rule"></div>
<a class="abs facts-more">Read More »</a>
<div class="abs divider"></div>

<div class="abs news" style="top:759px">
  <div class="news-date"><b>01</b><i>APR</i></div>
  <div><h4>We manage your activity</h4><p>Lorem ipsum dolor sit amet ampera mera monyok liwat kene aku tr[...]</p></div>
</div>
<div class="abs news" style="top:829px">
  <div class="news-date"><b>03</b><i>APR</i></div>
  <div><h4>We manage your activity</h4><p>Lorem ipsum dolor sit amet ampera mera monyok liwat kene aku tr[...]</p></div>
</div>
<a class="abs more-news">More News</a>

<footer class="abs footer"></footer>
<h3 class="abs f-head" style="left:137px;top:957px">Testimonials</h3>
<h3 class="abs f-head" style="left:497px;top:957px">Quick Links</h3>
<h3 class="abs f-head" style="left:637px;top:957px">Follow Us</h3>
<h3 class="abs f-head" style="left:764px;top:957px">Contact Us</h3>

<div class="abs testi">
  <svg class="abs" style="left:12px;top:52px" width="12" height="24" viewBox="0 0 12 24"><path d="M10 2L2 12l8 10" stroke="#2fa9e0" fill="none" stroke-width="1.5"/></svg>
  <svg class="abs" style="left:292px;top:52px" width="12" height="24" viewBox="0 0 12 24"><path d="M2 2l8 10-8 10" stroke="#2fa9e0" fill="none" stroke-width="1.5"/></svg>
  <div class="testi-photo" role="img" aria-label="Portrait of the company CEO"></div>
  <p class="testi-quote">"Lorem ipsum dolor sit amet cotetur adipi scing elit. ullam on etus et or portti tort velit nibh."</p>
  <p class="testi-name"><span>Lorem ipsum</span>, CEO</p>
</div>
<svg class="abs" style="left:150px;top:1120px" width="16" height="12" viewBox="0 0 16 12"><path d="M0 12L3 0h13z" fill="#fff"/></svg>

<ul class="abs links" style="left:497px;top:994px">
  <li>Home</li><li>About</li><li>Producsts</li><li>Ask A Question</li><li>Contact Us</li>
</ul>
<ul class="abs links follow" style="left:637px;top:993px">
  <li><span class="soc" style="background:#3b5998"></span><a>Friendloop</a></li>
  <li><span class="soc" style="background:#2fa9e0"></span><a>Chirpline</a></li>
  <li><span class="soc" style="background:#d0d0d0"></span><a>Circleweb +</a></li>
  <li><span class="soc" style="background:#1a7ab8"></span><a>ProNetwork</a></li>
  <li><span class="soc" style="background:#e2e2e2"></span><a>ClipStream</a></li>
</ul>

<div class="abs field" style="top:993px">Name</div>
<div class="abs field" style="top:1021px">Phone</div>
<div class="abs field" style="top:1048px">Email Address</div>
<div class="abs field" style="top:1075px;height:43px">Message</div>
<div class="abs submit">SUBMIT</div>

<div class="abs copy">© 2014 VantoMedix. All Rights Reserved</div>

</body>
</html>
```